Need A Standard Musical Download Website

We are looking for a talented designer to create a unique web design for our startup Music website called Zundo Music.
The website should be responsive and filled with some creative stuffs along with bright colors.

Zundo music is a website loaded with different types of music and capable of downloading the requested music by its users.
There will be categories of music which would be sorted by the genre. They include RnB, Hip-Hop, Afro pop, Pop, Dancehall and Reggae).

DESIGN STYLE/THEME

Creative, trendy, colorful, unique, and easy to use. You have freedom of selecting which ever color suits you. The design must be energetic and attractive.

NAVIGATION

HOME-MUSIC(RnB, Hip hop, Afro pop, POP, dancehall, Reggae)-ARTISTE-NEWS-LOGIN

PAGES REQUIRED
------------
1)Home Page
2)Music

FONTS
GOOGLE FONTS is strongly recommended.

Designers can get inspiration from https://tunevarok.com

Industry/Entity Type

Startup

```html
<!DOCTYPE html>
<html lang="en">
<head>
<meta charset="utf-8">
<title>Zundo Music</title>
<link rel="stylesheet" href="https://fonts.googleapis.com/css2?family=Roboto:wght@400;500;700&family=Roboto+Slab:wght@700&display=swap">
<style>
:root{
  --teal:#2499a6;
  --teal-bright:#2fd8e6;
  --red:#e2402d;
  --navy:#151a2b;
  --page:#efefef;
  --white:#ffffff;
  --footer-text:#b9bcc6;
  --caption:rgba(20,22,32,.78);
}
*{margin:0;padding:0;box-sizing:border-box}
html,body{width:1200px;height:2620px;overflow:hidden}
body{background:var(--page);font-family:"Roboto",Arial,sans-serif;position:relative}
.abs{position:absolute}

/* header */
.hero{left:0;top:0;width:1200px;height:590px;background:linear-gradient(135deg,#0f2335 0%,#143a4e 35%,#0c1f33 65%,#0a1a2c 100%)}
.hero-photo{left:0;top:0;width:1200px;height:590px;background:radial-gradient(circle at 30% 30%,rgba(40,150,170,.35),transparent 45%),radial-gradient(circle at 75% 75%,rgba(30,110,140,.3),transparent 40%)}
.brand{left:44px;top:22px;font-family:"Roboto Slab",Georgia,serif;font-weight:700;font-size:30px;color:var(--white);letter-spacing:-.5px}
.nav{top:32px;left:0;width:1200px;height:24px}
.nav a{position:absolute;color:var(--white);font-weight:700;font-size:18px;text-decoration:none;top:0}
.hero-title{left:0;top:145px;width:1200px;text-align:center;font-family:"Roboto Slab",Georgia,serif;font-weight:700;font-size:45px;line-height:58px;color:var(--white)}
.hero-title .accent{color:var(--teal-bright)}
.genres{left:0;top:349px;width:1200px;text-align:center;color:var(--white);font-weight:700;font-size:12px}
.search{left:285px;top:376px;width:644px;height:57px;border:2px solid var(--teal);border-radius:3px;background:rgba(30,35,48,.85);display:flex;align-items:center;padding-left:16px;color:#3b4150;font-size:18px;gap:12px}
.find-btn{left:493px;top:458px;width:214px;height:52px;background:var(--red);border-radius:2px;color:var(--white);font-weight:700;font-size:27px;display:flex;align-items:center;justify-content:center}

/* discover */
.discover{left:0;top:590px;width:1200px;height:362px;background:linear-gradient(180deg,var(--teal) 0%,var(--teal) 62%,#bfe2e6 82%,var(--white) 92%,var(--page) 100%)}
.compass{left:552px;top:625px}
.discover-title{left:0;top:710px;width:1200px;text-align:center;font-size:70px;line-height:80px;font-weight:700;color:var(--white)}

/* sections */
.section-title{left:28px;font-size:37px;line-height:44px;font-weight:500;color:var(--teal)}
.rule{left:28px;width:1144px;height:2px;background:var(--teal)}
.more{left:1107px;width:58px;height:16px;display:flex;justify-content:space-between}
.more span{width:15px;height:15px;border-radius:50%;background:var(--teal)}
.card{width:369px;height:368px;overflow:hidden;box-shadow:0 2px 3px rgba(0,0,0,.2)}
.card .photo{position:absolute;inset:0}
.photo-stage{background:linear-gradient(160deg,#3a4556 0%,#222a38 55%,#161b26 100%)}
.photo-guitar{background:linear-gradient(150deg,#3a3c46 0%,#24262f 60%,#1b1d25 100%)}
.photo-amp{background:linear-gradient(150deg,#6a4a43 0%,#3b3f4a 45%,#2a3140 100%)}
.card .caption{position:absolute;left:0;bottom:0;width:100%;height:58px;background:var(--caption);color:#e8e8ec;font-size:19px;padding:17px 0 0 22px}
.card .play{position:absolute;left:275px;top:279px;width:64px;height:64px;border-radius:50%;background:var(--red);display:flex;align-items:center;justify-content:center}

/* footer */
.footer{left:0;top:2388px;width:1200px;height:232px;background:var(--navy)}
.footer-brand{left:44px;top:2418px;font-family:"Roboto Slab",Georgia,serif;font-weight:700;font-size:30px;color:var(--footer-text)}
.footer-nav{left:442px;top:2432px;display:flex;gap:18px}
.footer-nav a{color:var(--footer-text);font-weight:700;font-size:18px;text-decoration:none}
.footer-rule{left:416px;top:2506px;width:368px;height:1px;background:#262b3c}
.social{left:1040px;top:2430px;display:flex;gap:14px}
.social span{width:30px;height:30px;border-radius:50%;background:#262b3c}
.copyright{left:0;top:2582px;width:1200px;text-align:center;color:var(--footer-text);font-size:12px}
</style>
</head>
<body>

<header class="abs hero">
  <div class="abs hero-photo" role="img" aria-label="Dim photo of studio music equipment in teal light"></div>
</header>
<div class="abs brand">Zundo Music</div>
<nav class="abs nav">
  <a href="#" style="left:709px">HOME</a>
  <a href="#" style="left:809px">MUSIC</a>
  <a href="#" style="left:908px">ARTIST</a>
  <a href="#" style="left:1008px">NEWS</a>
  <a href="#" style="left:1107px">LOGIN</a>
</nav>
<h1 class="abs hero-title">Find <span class="accent">Music.</span><br>Download It.<br>That Simple.</h1>
<div class="abs genres">RnB &nbsp;|&nbsp; Hip-Hop &nbsp;|&nbsp; Afro pop &nbsp;|&nbsp; Pop &nbsp;|&nbsp; Dancehall &nbsp;|&nbsp; Reggae</div>
<div class="abs search">
  <svg width="26" height="26" viewBox="0 0 26 26"><circle cx="14" cy="11" r="8" fill="none" stroke="#3b4150" stroke-width="3"/><line x1="8" y1="17" x2="2" y2="23" stroke="#3b4150" stroke-width="3"/></svg>
  <span>Search</span>
</div>
<div class="abs find-btn">Find It!</div>

<section class="abs discover" role="img" aria-label="Teal sky with white clouds along the lower edge"></section>
<svg class="abs compass" width="96" height="96" viewBox="-48 -48 96 96">
  <g fill="#ffffff">
    <polygon points="0,-48 9,-9 48,0 9,9 0,48 -9,9 -48,0 -9,-9"/>
    <polygon points="-22,-22 -5,-10 -10,-5"/><polygon points="22,-22 10,-5 5,-10"/>
    <polygon points="-22,22 -10,5 -5,10"/><polygon points="22,22 5,10 10,5"/>
    <circle r="8" fill="#2499a6"/><circle r="4"/>
  </g>
</svg>
<div class="abs discover-title">Discover</div>

<!-- Popular -->
<h2 class="abs section-title" style="top:974px">Popular</h2>
<div class="abs more" style="top:990px"><span></span><span></span><span></span></div>
<div class="abs rule" style="top:1017px"></div>

<div class="abs card" style="left:28px;top:1036px"><div class="photo photo-stage" role="img" aria-label="Live band performing on a dark stage"></div><div class="caption">Song Name - Artist</div><div class="play"><svg width="34" height="34" viewBox="0 0 34 34"><path d="M11 6 L29 2 V24 a5 5 0 1 1 -3 -4.6 V9 L14 11.5 V28 a5 5 0 1 1 -3 -4.6 Z" fill="#fff"/></svg></div></div>
<div class="abs card" style="left:416px;top:1036px"><div class="photo photo-stage" role="img" aria-label="Live band performing on a dark stage"></div><div class="caption">Song Name - Artist</div><div class="play"><svg width="34" height="34" viewBox="0 0 34 34"><path d="M11 6 L29 2 V24 a5 5 0 1 1 -3 -4.6 V9 L14 11.5 V28 a5 5 0 1 1 -3 -4.6 Z" fill="#fff"/></svg></div></div>
<div class="abs card" style="left:803px;top:1036px"><div class="photo photo-stage" role="img" aria-label="Live band performing on a dark stage"></div><div class="caption">Song Name - Artist</div><div class="play"><svg width="34" height="34" viewBox="0 0 34 34"><path d="M11 6 L29 2 V24 a5 5 0 1 1 -3 -4.6 V9 L14 11.5 V28 a5 5 0 1 1 -3 -4.6 Z" fill="#fff"/></svg></div></div>
<svg class="abs" style="left:590px;top:1416px" width="20" height="12" viewBox="0 0 20 12"><polygon points="0,0 20,0 10,11" fill="#a9a9ad"/></svg>

<!-- Artists -->
<h2 class="abs section-title" style="top:1440px">Artists</h2>
<div class="abs more" style="top:1456px"><span></span><span></span><span></span></div>
<div class="abs rule" style="top:1484px"></div>

<div class="abs card" style="left:28px;top:1502px"><div class="photo photo-guitar" role="img" aria-label="Close-up of hands playing an electric guitar"></div><div class="caption">Artist Name</div><div class="play"><svg width="34" height="34" viewBox="0 0 34 34"><path d="M11 6 L29 2 V24 a5 5 0 1 1 -3 -4.6 V9 L14 11.5 V28 a5 5 0 1 1 -3 -4.6 Z" fill="#fff"/></svg></div></div>
<div class="abs card" style="left:416px;top:1502px"><div class="photo photo-guitar" role="img" aria-label="Close-up of hands playing an electric guitar"></div><div class="caption">Artist Name</div><div class="play"><svg width="34" height="34" viewBox="0 0 34 34"><path d="M11 6 L29 2 V24 a5 5 0 1 1 -3 -4.6 V9 L14 11.5 V28 a5 5 0 1 1 -3 -4.6 Z" fill="#fff"/></svg></div></div>
<div class="abs card" style="left:803px;top:1502px"><div class="photo photo-guitar" role="img" aria-label="Close-up of hands playing an electric guitar"></div><div class="caption">Artist Name</div><div class="play"><svg width="34" height="34" viewBox="0 0 34 34"><path d="M11 6 L29 2 V24 a5 5 0 1 1 -3 -4.6 V9 L14 11.5 V28 a5 5 0 1 1 -3 -4.6 Z" fill="#fff"/></svg></div></div>

<!-- Albums -->
<h2 class="abs section-title" style="top:1905px">Albums</h2>
<div class="abs more" style="top:1921px"><span></span><span></span><span></span></div>
<div class="abs rule" style="top:1950px"></div>

<div class="abs card" style="left:28px;top:1967px"><div class="photo photo-amp" role="img" aria-label="Guitar amplifier beside an electric guitar"></div><div class="caption">Album Name - Artist</div><div class="play"><svg width="34" height="34" viewBox="0 0 34 34"><path d="M11 6 L29 2 V24 a5 5 0 1 1 -3 -4.6 V9 L14 11.5 V28 a5 5 0 1 1 -3 -4.6 Z" fill="#fff"/></svg></div></div>
<div class="abs card" style="left:416px;top:1967px"><div class="photo photo-amp" role="img" aria-label="Guitar amplifier beside an electric guitar"></div><div class="caption">Album Name - Artist</div><div class="play"><svg width="34" height="34" viewBox="0 0 34 34"><path d="M11 6 L29 2 V24 a5 5 0 1 1 -3 -4.6 V9 L14 11.5 V28 a5 5 0 1 1 -3 -4.6 Z" fill="#fff"/></svg></div></div>
<div class="abs card" style="left:803px;top:1967px"><div class="photo photo-amp" role="img" aria-label="Guitar amplifier beside an electric guitar"></div><div class="caption">Album Name - Artist</div><div class="play"><svg width="34" height="34" viewBox="0 0 34 34"><path d="M11 6 L29 2 V24 a5 5 0 1 1 -3 -4.6 V9 L14 11.5 V28 a5 5 0 1 1 -3 -4.6 Z" fill="#fff"/></svg></div></div>

<!-- Footer -->
<footer class="abs footer"></footer>
<div class="abs footer-brand">Zundo Music</div>
<nav class="abs footer-nav"><a href="#">Home</a><a href="#">Music</a><a href="#">Artist</a><a href="#">News</a><a href="#">Login</a></nav>
<div class="abs social"><span></span><span></span><span></span></div>
<div class="abs footer-rule"></div>
<div class="abs copyright">Zundo Music © Copyright 2017</div>

</body>
</html>
```